Business Cards and Letterhead
for Modern Boston Law Firm
Simple
Gerald Dunmore
71 Ashworth Street
3rd Floor
Brookline, Massachusetts 02446
ger@dunmorekp-example.com
www.dunmorekp-example.com

```html
<!DOCTYPE html>
<html lang="en">
<head>
<meta charset="utf-8">
<title>Dunmore Law Group – Business Card</title>
<link rel="stylesheet" href="https://fonts.googleapis.com/css2?family=Roboto+Condensed:wght@400;700&display=swap">
<style>
  :root {
    --backdrop: #d6d6d6;
    --card: #ffffff;
    --brand-red: #b5121b;
    --ink: #4a4a4a;
    --rule: #c9c9c9;
    --text-font: "Roboto Condensed", Arial, sans-serif;
  }
  * { box-sizing: border-box; margin: 0; padding: 0; }
  html, body {
    width: 1200px;
    height: 874px;
    overflow: hidden;
    background: var(--backdrop);
    font-family: var(--text-font);
  }
  .business-card {
    position: absolute;
    left: 120px;
    top: 163px;
    width: 960px;
    height: 548px;
    background: var(--card);
    border-radius: 30px;
    box-shadow: 0 10px 30px rgba(0,0,0,0.18);
    overflow: hidden;
  }
  .firm-mark {
    position: absolute;
    left: 70px;
    top: 150px;
    display: flex;
    align-items: center;
    gap: 18px;
  }
  .firm-mark__dot {
    width: 56px;
    height: 56px;
    border-radius: 50%;
    background: var(--brand-red);
    flex: none;
  }
  .firm-mark__name {
    font-weight: 700;
    font-size: 46px;
    letter-spacing: 1px;
    color: var(--brand-red);
    text-transform: uppercase;
    white-space: nowrap;
  }
  .person-name {
    position: absolute;
    left: 70px;
    top: 330px;
    font-weight: 700;
    font-size: 38px;
    line-height: 46px;
    color: var(--brand-red);
  }
  .divider {
    position: absolute;
    left: 70px;
    right: 70px;
    top: 388px;
    height: 2px;
    background: var(--rule);
  }
  .contact {
    position: absolute;
    top: 404px;
    font-size: 19px;
    line-height: 30px;
    color: var(--ink);
    font-style: normal;
    white-space: nowrap;
  }
  .contact--address { left: 70px; }
  .contact--phones { left: 400px; }
  .contact--online { left: 580px; }
  .contact__line {
    display: flex;
    align-items: center;
    gap: 8px;
  }
  .contact__icon {
    width: 16px;
    height: 16px;
    flex: none;
    fill: var(--brand-red);
  }
</style>
</head>
<body>
  <main class="business-card">
    <div class="firm-mark">
      <span class="firm-mark__dot"></span>
      <span class="firm-mark__name">Dunmore Law Group</span>
    </div>

    <h1 class="person-name">Gerald Dunmore</h1>
    <div class="divider"></div>

    <address class="contact contact--address">
      <div class="contact__line">71 Ashworth Street, 3rd Floor</div>
      <div class="contact__line">Brookline, Massachusetts 02446</div>
    </address>

    <div class="contact contact--phones">
      <div class="contact__line">
        <svg class="contact__icon" viewBox="0 0 24 24" aria-hidden="true"><path d="M6.6 10.8a15.1 15.1 0 0 0 6.6 6.6l2.2-2.2c.3-.3.7-.4 1-.2 1.1.4 2.3.6 3.6.6.6 0 1 .4 1 1V20c0 .6-.4 1-1 1A17 17 0 0 1 3 4c0-.6.4-1 1-1h3.5c.6 0 1 .4 1 1 0 1.3.2 2.5.6 3.6.1.3 0 .7-.2 1z"/></svg>
        617.555.0142
      </div>
      <div class="contact__line">
        <svg class="contact__icon" viewBox="0 0 24 24" aria-hidden="true"><path d="M6 3h10v5H6z M3 9h18v9h-3v3H6v-3H3z M8 15v4h8v-4z"/></svg>
        617.555.0187
      </div>
    </div>

    <div class="contact contact--online">
      <div class="contact__line">
        <svg class="contact__icon" viewBox="0 0 24 24" aria-hidden="true"><path d="M2 5h20v14H2z M4 7v.5l8 5.5 8-5.5V7z"/></svg>
        ger@dunmorekp-example.com
      </div>
      <div class="contact__line">
        <svg class="contact__icon" viewBox="0 0 24 24" aria-hidden="true"><circle cx="12" cy="12" r="10"/></svg>
        www.dunmorekp-example.com
      </div>
    </div>
  </main>
</body>
</html>
```